Condo Debts Collection Business needs a Web Design (Contest)

I need a site for a client, who works with condo debts collection, and ensure all revenues provided by condo fees will be always available to the building manager of condo on a specific date, regardless of defaults.I have the logo of the companies, and some requirements on layout (kind of slider, menu options, phone number on a noble position, etc).
Updates

Designs look the same

Target Market(s)

I have two targets for this design: - Condominium's building manager. This target is looking for a solution to overdue debts on it's condo. - Residents on condominiums. This target wants to live in a better place, where their neighbors pay their condominium fees on time.

Number of Pages Required

1 page

Requirements
Must have
• - Slider with title, some short text related, a nice image (I prefer happy and/or peaceful family, people doing business, happy friends, and so on).
• - I have a special attention to menu. I'm looking for one I can have a nice effect, more elegant, charming, kind of innovative.
• - Phone number on the top (or clearly visible).
• - Member log in area or icon on the top (or clearly visible).
• - News/articles area.
• - Modern fonts, with good quality, sans-serif on areas where reading is more intensive (prefer Google web-fonts).
• - Colors specified on attached files.
• - Header similar or inspired by the "FILE 3"
Nice to have
• - Clear background color, cause it's better to read larger texts (like articles). Dark backgrounds makes reading difficult.
• - A site with effects (like shadows, lines, gradients, lights) is usually pretty.
• - I pay attention on beautiful footers.
Should not have
• - Images with a lot of money (I don't sell richness, I sell tranquility, peace, harmony, safety).
• - Poor menu.
• - Lots of curves. My customer asked for straight lines.

```html
<!DOCTYPE html>
<html lang="en">
<head>
<meta charset="utf-8">
<title>Serenara – Condo Debts Collection</title>
<link href="https://fonts.googleapis.com/css2?family=Roboto:wght@300;400;500;700;900&display=swap" rel="stylesheet">
<style>
:root{
  --navy:#0f2f5e;
  --navy-deep:#0a2347;
  --orange:#ec6a1c;
  --text:#3c3c3c;
  --muted:#6b6b6b;
  --light:#f1f1f1;
  --white:#ffffff;
}
*{box-sizing:border-box;margin:0;padding:0}
html,body{width:1200px;height:4157px;overflow:hidden}
body{font-family:'Roboto',sans-serif;color:var(--text);background:var(--white);position:relative}
section,header,footer{position:relative;width:1200px;overflow:hidden}
.abs{position:absolute}

/* header */
.site-header{height:138px;background:var(--navy)}
.brand{left:130px;top:36px;display:flex;align-items:center;gap:12px;color:var(--white);font-weight:700;font-size:30px;letter-spacing:.5px}
.brand-mark{width:34px;height:34px;background:var(--orange)}
.call{left:565px;top:24px;display:flex;align-items:center;gap:12px;color:var(--white)}
.call small{display:block;font-size:15px}
.call strong{font-size:19px;font-weight:700}
.login{left:873px;top:22px;width:192px;height:40px;background:var(--orange);color:var(--white);font-size:15px;font-weight:500;display:flex;align-items:center;justify-content:center;gap:8px}
.main-nav{left:560px;top:94px;display:flex;gap:30px}
.main-nav a{color:var(--white);text-decoration:none;font-size:15px;font-weight:500}

/* hero */
.hero{height:640px;background:linear-gradient(180deg,#c6dbea 0%,#a9c9de 45%,#8fb6cb 60%,#d9d2c2 100%)}
.hero-photo{inset:0}
.hero-title{left:130px;top:188px;color:var(--navy);font-size:62px;line-height:1.15}
.hero-title b{font-weight:900;display:block}
.hero-title span{font-weight:300;display:block}
.btn-orange{background:var(--orange);color:var(--white);font-weight:500;font-size:17px;display:flex;align-items:center;justify-content:center}
.hero-btn{left:130px;top:362px;width:185px;height:46px}
.dots{left:132px;top:442px;display:flex;gap:6px}
.dots i{width:12px;height:12px;border-radius:50%;border:2px solid var(--navy);display:block}
.dots i:first-child{background:var(--navy)}

/* about */
.about{height:587px}
.about-photo{left:145px;top:110px;width:425px;height:347px;background:linear-gradient(135deg,#c9a788,#7c6b5e 55%,#3d3a3c);box-shadow:0 8px 18px rgba(0,0,0,.3);border:6px solid #fff}
.about-text{left:620px;top:112px;width:440px}
.eyebrow{font-size:18px;font-weight:500;color:var(--navy)}
.about-text h2{font-size:42px;font-weight:700;color:var(--navy);margin-top:4px}
.divider{margin:12px 0 16px}
.about-text p{font-size:15px;line-height:1.95;color:var(--muted)}
.btn-outline{display:inline-flex;margin-top:40px;width:132px;height:40px;border:2px solid var(--text);align-items:center;justify-content:center;font-size:14px;font-weight:500}

/* services */
.services{height:947px;background:linear-gradient(150deg,#0e2a55 0%,#1d3c68 35%,#6b4a3d 70%,#e8681a 100%)}
.section-title{width:100%;text-align:center;font-size:40px;font-weight:400}
.section-title b{font-weight:900}
.services .section-title{top:90px;color:var(--white)}
.arrow-center{left:560px}
.card{width:285px;height:270px;background:var(--white);text-align:center;padding-top:32px;box-shadow:0 6px 14px rgba(0,0,0,.25)}
.card h3{font-size:17px;font-weight:700;color:var(--text);margin:16px 0 10px}
.card p{font-size:14px;line-height:1.6;color:var(--muted);padding:0 32px}

/* testimonials */
.testimonials{height:636px;background:radial-gradient(ellipse at 50% 40%,#4a3f3b 0%,#2a2524 55%,#151313 100%)}
.testimonials .section-title{top:90px;color:var(--white)}
.quote{width:293px;height:217px;border:2px solid #e8e8e8;color:var(--white);text-align:center;padding:60px 26px 0}
.quote p{font-size:14.5px;line-height:1.55}
.quote .who{position:absolute;bottom:22px;left:0;width:100%;font-size:17px}
.avatar{width:94px;height:94px;border-radius:50%;border:3px solid #fff;background:linear-gradient(180deg,#b8b4b0,#4e4c50)}

/* news */
.news{height:687px}
.news .section-title{top:80px;color:#1a1a1a}
.post{width:284px;height:350px;background:var(--light);border-left:4px solid var(--orange);box-shadow:0 3px 8px rgba(0,0,0,.12)}
.post-photo{width:280px;height:180px}
.post-date{color:var(--orange);font-size:14px;font-weight:500;padding:20px 0 0 24px;display:flex;align-items:center;gap:8px}
.post p{font-size:14px;line-height:1.7;color:var(--muted);padding:10px 20px 0 24px}

/* footer */
.site-footer{height:380px;background:var(--light)}
.footer h4{font-size:20px;font-weight:700;color:#1e1e1e}
.contact-list{list-style:none}
.contact-list li{display:flex;gap:14px;font-size:15px;line-height:1.4;margin-top:18px;color:var(--text)}
.field{width:212px;height:40px;background:var(--white);border:1px solid #cfcfcf;font-size:12px;padding:12px 10px;color:var(--text)}
.social{width:34px;height:34px;border-radius:50%;border:2px solid var(--orange)}
.quick{list-style:none}
.quick li{font-size:14px;margin-top:8px;color:var(--text)}
.quick li::before{content:"›";margin-right:10px;color:var(--muted)}
.copyright{height:142px;text-align:center;font-size:14px;padding-top:62px;color:var(--text)}
</style>
</head>
<body>

<header class="site-header">
  <div class="abs brand"><span class="brand-mark"></span>SERENARA</div>
  <div class="abs call">
    <svg width="34" height="34" viewBox="0 0 34 34"><circle cx="17" cy="17" r="15" fill="none" stroke="#fff" stroke-width="2"/><path d="M12 10c1-1 2-1 3 0l1.5 2.5c.5 1 0 1.7-.8 2.3l-.7.5c.7 1.8 2 3.2 3.8 4l.6-.7c.6-.8 1.4-1.2 2.3-.7L24 19.5c1 .6 1 1.8 0 2.8l-1 1c-3.5 1.5-11-6-11.5-11z" fill="#fff"/></svg>
    <div><small>Call Us :</small><strong>4150-2210 / 4150-2220</strong></div>
  </div>
  <div class="abs login btn-orange">
    <svg width="14" height="16" viewBox="0 0 14 16"><rect x="1" y="7" width="12" height="9" fill="#fff"/><path d="M3.5 7V4.5a3.5 3.5 0 0 1 7 0V7" fill="none" stroke="#fff" stroke-width="2"/></svg>
    MEMBER LOGIN
  </div>
  <nav class="abs main-nav"><a href="#">HOME</a><a href="#">ABOUT US</a><a href="#">OUR SERVICES</a><a href="#">NEWS</a><a href="#">CONTACT US</a></nav>
</header>

<section class="hero">
  <div class="abs hero-photo" role="img" aria-label="Happy family walking hand in hand along a sunny beach"></div>
  <h1 class="abs hero-title"><b>CONDO DEBTS</b><span>COLLECTION</span></h1>
  <div class="abs hero-btn btn-orange">GET MORE INFO</div>
  <div class="abs dots"><i></i><i></i><i></i><i></i></div>
</section>

<section class="about">
  <div class="abs about-photo" role="img" aria-label="Business team meeting around a laptop"></div>
  <div class="abs about-text">
    <div class="eyebrow">WELCOME TO</div>
    <h2>SERENARA</h2>
    <svg class="divider" width="80" height="12" viewBox="0 0 80 12"><line x1="0" y1="6" x2="80" y2="6" stroke="#0f2f5e" stroke-width="2"/><path d="M30 1l14 5-14 5z" fill="#ec6a1c"/></svg>
    <p>Sed ut perspiciatis unde omnis iste natus error sit voluptatem accusantium doloremque laudantium, totam rem aperiam, eaque ipsa quae ab illo inventore veritatis et quasi architecto beatae vitae dicta sunt explicabo. Nemo enim ipsam voluptatem quia voluptas sit aspernatur aut odit aut fugit, sed</p>
    <span class="btn-outline">READ MORE</span>
  </div>
</section>

<section class="services">
  <h2 class="abs section-title"><b>OUR</b> SERVICES</h2>
  <svg class="abs arrow-center" style="top:170px" width="80" height="14" viewBox="0 0 80 14"><line x1="0" y1="7" x2="76" y2="7" stroke="#fff" stroke-width="2"/><path d="M66 1l14 6-14 6z" fill="#fff"/></svg>

  <div class="abs card" style="left:145px;top:250px">
    <svg width="70" height="70" viewBox="0 0 70 70" fill="none" stroke="#ec6a1c" stroke-width="2.5"><rect x="16" y="8" width="38" height="50"/><line x1="24" y1="40" x2="46" y2="40"/><line x1="24" y1="48" x2="40" y2="48"/><path d="M35 16v14M28 23h14"/><path d="M8 48l14 14h30"/></svg>
    <h3>QUIS AUTEM VEL EUM</h3><p>Sed ut perspiciatis unde omnis iste natussit voluptatem accusantium doloremque latam rem</p>
  </div>
  <div class="abs card" style="left:455px;top:250px">
    <svg width="70" height="70" viewBox="0 0 70 70" fill="none" stroke="#ec6a1c" stroke-width="2.5"><rect x="10" y="14" width="50" height="34"/><line x1="35" y1="48" x2="35" y2="58"/><line x1="24" y1="58" x2="46" y2="58"/><path d="M22 26h26l-3 12H25z"/><circle cx="28" cy="42" r="1.5"/><circle cx="42" cy="42" r="1.5"/></svg>
    <h3>QUIS AUTEM VEL EUM</h3><p>Sed ut perspiciatis unde omnis iste natussit voluptatem accusantium doloremque latam rem</p>
  </div>
  <div class="abs card" style="left:767px;top:250px">
    <svg width="70" height="70" viewBox="0 0 70 70" fill="none" stroke="#ec6a1c" stroke-width="2.5"><rect x="10" y="12" width="42" height="46"/><line x1="10" y1="22" x2="52" y2="22"/><line x1="18" y1="32" x2="36" y2="32"/><line x1="18" y1="40" x2="30" y2="40"/><rect x="38" y="34" width="22" height="26"/><line x1="44" y1="44" x2="54" y2="44"/></svg>
    <h3>QUIS AUTEM VEL EUM</h3><p>Sed ut perspiciatis unde omnis iste natussit voluptatem accusantium doloremque latam rem</p>
  </div>
  <div class="abs card" style="left:145px;top:543px">
    <svg width="70" height="70" viewBox="0 0 70 70" fill="none" stroke="#ec6a1c" stroke-width="2.5"><circle cx="35" cy="16" r="8"/><line x1="35" y1="24" x2="35" y2="34"/><path d="M18 44l17-10 17 10"/><circle cx="18" cy="48" r="5"/><circle cx="35" cy="48" r="5"/><circle cx="52" cy="48" r="5"/><path d="M10 62a8 8 0 0 1 16 0M27 62a8 8 0 0 1 16 0M44 62a8 8 0 0 1 16 0"/></svg>
    <h3>QUIS AUTEM VEL EUM</h3><p>Sed ut perspiciatis unde omnis iste natussit voluptatem accusantium doloremque latam rem</p>
  </div>
  <div class="abs card" style="left:455px;top:543px">
    <svg width="70" height="70" viewBox="0 0 70 70" fill="none" stroke="#ec6a1c" stroke-width="2.5"><rect x="8" y="12" width="54" height="44"/><rect x="16" y="40" width="7" height="12"/><rect x="28" y="34" width="7" height="18"/><rect x="40" y="28" width="7" height="24"/><path d="M16 32l12-8 10 4 14-10"/><path d="M46 16h6v6"/></svg>
    <h3>QUIS AUTEM VEL EUM</h3><p>Sed ut perspiciatis unde omnis iste natussit voluptatem accusantium doloremque latam rem</p>
  </div>
  <div class="abs card" style="left:767px;top:543px">
    <svg width="70" height="70" viewBox="0 0 70 70" fill="none" stroke="#ec6a1c" stroke-width="2.5"><rect x="24" y="8" width="38" height="30"/><path d="M30 30l8-8 6 5 12-12"/><circle cx="16" cy="30" r="6"/><path d="M6 60V46a10 10 0 0 1 20 0v14"/><line x1="26" y1="42" x2="40" y2="38"/><line x1="30" y1="60" x2="60" y2="60"/></svg>
    <h3>QUIS AUTEM VEL EUM</h3><p>Sed ut perspiciatis unde omnis iste natussit voluptatem accusantium doloremque latam rem</p>
  </div>
</section>

<section class="testimonials" role="img" aria-label="Dimmed photo of a smiling woman working at a laptop">
  <h2 class="abs section-title"><b>CLIENT</b> TESTIMONIALS</h2>
  <svg class="abs arrow-center" style="top:170px" width="80" height="12" viewBox="0 0 80 12"><line x1="0" y1="6" x2="80" y2="6" stroke="#fff" stroke-width="2"/><path d="M30 1l14 5-14 5z" fill="#ec6a1c"/></svg>

  <div class="abs quote" style="left:145px;top:296px"><p>Sed ut perspiciatis unde omnis iste natus error sit voluptatem accusantium doloremque laudantium, totam rem aperiam, eaque ipsa quae ab</p><div class="who">Lemaire, B.</div></div>
  <div class="abs avatar" style="left:245px;top:243px" role="img" aria-label="Client portrait"></div>

  <div class="abs quote" style="left:455px;top:296px"><p>Sed ut perspiciatis unde omnis iste natus error sit voluptatem accusantium doloremque laudantium, totam rem aperiam, eaque ipsa quae ab</p><div class="who">Lemaire, B.</div></div>
  <div class="abs avatar" style="left:555px;top:243px" role="img" aria-label="Client portrait"></div>

  <div class="abs quote" style="left:762px;top:296px"><p>Sed ut perspiciatis unde omnis iste natus error sit voluptatem accusantium doloremque laudantium, totam rem aperiam, eaque ipsa quae</p><div class="who">Lemaire, B.</div></div>
  <div class="abs avatar" style="left:862px;top:243px" role="img" aria-label="Client portrait"></div>
</section>

<section class="news">
  <h2 class="abs section-title"><b>LATEST</b> NEWS</h2>
  <svg class="abs arrow-center" style="top:160px" width="80" height="12" viewBox="0 0 80 12"><line x1="0" y1="6" x2="80" y2="6" stroke="#0f2f5e" stroke-width="2"/><path d="M30 1l14 5-14 5z" fill="#ec6a1c"/></svg>

  <article class="abs post" style="left:133px;top:227px">
    <div class="post-photo" role="img" aria-label="Hands working over papers on a desk" style="background:linear-gradient(135deg,#6f4a4a,#c5a9a0 60%,#8a6c64)"></div>
    <div class="post-date"><svg width="14" height="14" viewBox="0 0 14 14"><rect x="1" y="2" width="12" height="11" fill="none" stroke="#ec6a1c" stroke-width="1.5"/><line x1="1" y1="6" x2="13" y2="6" stroke="#ec6a1c" stroke-width="1.5"/></svg>October 17, 2019</div>
    <p>Sed ut perspiciatis unde omnis iste natus error sit voluptatem accusantium doloremque laudantium, totam rem aperiam, eaque ipsa quae ab illo</p>
  </article>
  <article class="abs post" style="left:457px;top:227px">
    <div class="post-photo" role="img" aria-label="Family playing in a field at sunset" style="background:linear-gradient(180deg,#f3b45a,#c46a28 55%,#4d3a1f)"></div>
    <div class="post-date"><svg width="14" height="14" viewBox="0 0 14 14"><rect x="1" y="2" width="12" height="11" fill="none" stroke="#ec6a1c" stroke-width="1.5"/><line x1="1" y1="6" x2="13" y2="6" stroke="#ec6a1c" stroke-width="1.5"/></svg>October 17, 2019</div>
    <p>Sed ut perspiciatis unde omnis iste natus error sit voluptatem accusantium doloremque laudantium, totam rem aperiam, eaque ipsa quae ab illo</p>
  </article>
  <article class="abs post" style="left:782px;top:227px">
    <div class="post-photo" role="img" aria-label="Team planning with sticky notes on a table" style="background:linear-gradient(135deg,#4a4a4e,#b8b0b4 55%,#d77a9a)"></div>
    <div class="post-date"><svg width="14" height="14" viewBox="0 0 14 14"><rect x="1" y="2" width="12" height="11" fill="none" stroke="#ec6a1c" stroke-width="1.5"/><line x1="1" y1="6" x2="13" y2="6" stroke="#ec6a1c" stroke-width="1.5"/></svg>October 17, 2019</div>
    <p>Sed ut perspiciatis unde omnis iste natus error sit voluptatem accusantium doloremque laudantium, totam rem aperiam, eaque ipsa quae ab illo</p>
  </article>
</section>

<footer class="site-footer footer">
  <div class="abs" style="left:130px;top:80px;width:280px">
    <h4>CONTACT US</h4>
    <ul class="contact-list" style="margin-top:14px">
      <li><svg width="16" height="20" viewBox="0 0 16 20"><path d="M8 0a7 7 0 0 1 7 7c0 5-7 13-7 13S1 12 1 7a7 7 0 0 1 7-7z" fill="#ec6a1c"/><circle cx="8" cy="7" r="2.5" fill="#fff"/></svg><span>Serenara 12/5, Riverside,<br>110 00 Lumen 3</span></li>
      <li><svg width="16" height="16" viewBox="0 0 16 16"><path d="M2 1c1-1 2-1 3 0l2 3c.5 1 0 2-1 2.5C7 9 8 10 9.5 10.5 10 9.5 11 9 12 9.5l3 2c1 1 1 2 0 3l-1 1C9 16 0 7 1 2z" fill="#ec6a1c"/></svg><span>Phone:<br>4150-2210 / 4150-2220</span></li>
      <li><svg width="16" height="14" viewBox="0 0 16 14"><rect x="0" y="1" width="16" height="12" fill="#ec6a1c"/><path d="M0 1l8 7 8-7" fill="none" stroke="#fff" stroke-width="1.5"/></svg><span>Email:<br>contact@serenara-example.com</span></li>
    </ul>
  </div>

  <div class="abs" style="left:445px;top:74px;width:440px">
    <h4>GET A QUICK NOW!</h4>
    <div style="display:grid;grid-template-columns:212px 212px;gap:8px 16px;margin-top:24px">
      <div class="field">Your Name</div><div class="field">Your E - Mail</div>
      <div class="field">Your Phone</div><div class="field">Message</div>
    </div>
    <div style="display:flex;align-items:center;gap:16px;margin-top:10px">
      <div class="btn-orange" style="width:212px;height:36px;font-size:15px">SUBMIT</div>
      <span class="social"></span><span class="social" style="margin-left:-10px"></span>
    </div>
  </div>

  <div class="abs" style="left:952px;top:80px">
    <h4>QUICK LINK</h4>
    <ul class="quick" style="margin-top:12px">
      <li>Home</li><li>About us</li><li>Our Services</li><li>Reviews</li><li>Blog</li><li>Contact Us</li>
    </ul>
  </div>
</footer>

<div class="copyright">©2019 Serenara. All Rights Reserved. Disclaimer &nbsp;|&nbsp; Privacy policy &nbsp;|&nbsp; Terms of use</div>

</body>
</html>
```